movie poster for a bittersweet romantic drama

Hello everyone. Looking for a dynamic poster for feature film 'Maple's Lantern' a romantic drama. It is a bittersweet love story so not rosey lovie dovie type.

300dpi

Please visit the link below for the poster image
https://www.filecrate.example/s/k7x2p41hrq9zt5m/_R8K4417.tif?dl=0

poster should have:
1. title of film : Maple's Lantern
2. tagline of film:
Death knows no names
Love does not know race

3. A film by Harriet B. Okonkwe
4 Include the logo for 'Tolubi Pictures' attached below

poster size:
1. 8x10
2. thumnail
3. landscape with just film title
4. 27 by 41

Target Market(s)

15-55 men and mostly women

Industry/Entity Type

Film Production

Colors

Designer to choose colors to be used in the design.

Requirements
Must have
• Dynamic and vibrant
• it is a romantic drama so love on a serious note
Nice to have
• Play with romantic fonts but don't overdo it.
Should not have
• must not look like a romance novel

```html
<!DOCTYPE html>
<html lang="en">
<head>
<meta charset="utf-8">
<title>Maple's Lantern — Poster</title>
<link rel="stylesheet" href="https://fonts.googleapis.com/css2?family=Jost:wght@300;700&family=Playfair+Display:wght@400&display=swap">
<style>
  :root {
    --sky-deep: #5ba6e6;
    --sky-light: #a9cff2;
    --hill-teal: #4f7a6a;
    --hill-sage: #7b9a86;
    --field-yellow: #d9dc2a;
    --field-green: #3fae2f;
    --scrub-dark: #3e5a2e;
    --soil-orange: #d58a5a;
    --ink-white: #ffffff;
    --ink-navy: #1c3f8a;
  }
  html, body {
    margin: 0;
    padding: 0;
    width: 959px;
    height: 1200px;
    overflow: hidden;
    background: var(--sky-deep);
  }
  .poster {
    position: relative;
    width: 959px;
    height: 1200px;
    overflow: hidden;
    background: linear-gradient(to bottom,
      var(--sky-deep) 0%,
      var(--sky-light) 18%,
      var(--sky-light) 78%,
      var(--sky-deep) 100%);
  }
  .landscape {
    position: absolute;
    left: 0;
    top: 212px;
    width: 959px;
    height: 740px;
    background: linear-gradient(to bottom,
      var(--hill-sage) 0%,
      var(--hill-teal) 12%,
      var(--hill-sage) 20%,
      var(--soil-orange) 27%,
      var(--field-yellow) 32%,
      var(--field-green) 40%,
      var(--scrub-dark) 50%,
      var(--field-green) 60%,
      var(--field-yellow) 68%,
      var(--soil-orange) 73%,
      var(--hill-sage) 80%,
      var(--hill-teal) 88%,
      var(--hill-sage) 100%);
  }
  .tagline {
    position: absolute;
    top: 52px;
    left: 0;
    width: 959px;
    margin: 0;
    text-align: center;
    font-family: 'Jost', sans-serif;
    font-weight: 300;
    font-size: 29px;
    letter-spacing: 0.5px;
    color: var(--ink-white);
    white-space: nowrap;
  }
  .tagline strong { font-weight: 700; }
  .title {
    position: absolute;
    left: 0;
    top: 410px;
    width: 959px;
    margin: 0;
    text-align: center;
    font-family: 'Playfair Display', serif;
    font-weight: 400;
    font-size: 138px;
    line-height: 146px;
    letter-spacing: -1px;
    color: var(--ink-white);
    text-transform: uppercase;
  }
  .title span { display: block; }
  .credit {
    position: absolute;
    top: 706px;
    right: 180px;
    margin: 0;
    font-family: 'Jost', sans-serif;
    font-weight: 700;
    font-size: 18px;
    letter-spacing: 1.5px;
    color: var(--ink-white);
    text-transform: uppercase;
  }
  .studio {
    position: absolute;
    right: 50px;
    bottom: 70px;
    display: flex;
    align-items: center;
    gap: 10px;
    font-family: 'Jost', sans-serif;
    font-weight: 700;
    font-size: 24px;
    color: var(--ink-navy);
    text-transform: uppercase;
    letter-spacing: 1px;
  }
  .studio-dot {
    width: 26px;
    height: 26px;
    border-radius: 50%;
    background: var(--ink-navy);
  }
</style>
</head>
<body>
  <main class="poster">
    <div class="landscape" role="img" aria-label="Mirrored photograph of rolling hills and fields of yellow wildflowers and green grass reflected in still water"></div>
    <p class="tagline"><strong>DEATH</strong> KNOWS NO NAMES &nbsp;<strong>LOVE</strong> DOES NOT KNOW RACE</p>
    <h1 class="title"><span>Maple’s</span><span>Lantern</span></h1>
    <p class="credit">A film by Harriet B. Okonkwe</p>
    <div class="studio"><span class="studio-dot"></span><span>Tolubi Pictures</span></div>
  </main>
</body>
</html>
```